Harborline Energy - needs a business card

Harborline Energy is a U.S. based diesel sourcing and distribution company that supports American oil & gas fields through providing quality product and consistent services.

Target Market(s)

Oil and Gas

Contact Information for Business Card

The background of the card must be white to ensure the logo pops.

Font styles to use
Serif
Sans Serif

Colors

Designer to choose colors to be used in the design.

Requirements
Must have
• Front of Card: Tag line: Harborline Energy, Powering America's Oil & Gas fields.
• Not sure if you guys do this part but just in case...
• Dale Menschow
• Owner/CEO
• C:555.318.4076
• E:Dmenschow@harborlineenergy.example
• W:Harborlineenergy.example
• Locations: Servicing the Powder River, DJ basin and Bakken formations.
• Back of Card: " Frac fueling is what we do. We understand how important diesel fuel is to your operation, which is why our main service line is Frac fueling. We assure our supply and stand by our service"

```html
<!DOCTYPE html>
<html lang="en">
<head>
<meta charset="utf-8">
<title>Harborline Energy – Business Card</title>
<link href="https://fonts.googleapis.com/css2?family=Poppins:wght@300;400;600;700&display=swap" rel="stylesheet">
<style>
  :root {
    --navy: #1d2f63;
    --red: #c8202f;
    --white: #ffffff;
    --grey-text: #5b6170;
    --backdrop: #e6e7ea;
  }
  * { box-sizing: border-box; margin: 0; padding: 0; }
  html, body { width: 1200px; height: 870px; overflow: hidden; }
  body {
    background: var(--backdrop);
    font-family: "Poppins", sans-serif;
    position: relative;
  }
  .card {
    position: absolute;
    top: 280px;
    width: 540px;
    height: 310px;
    border-radius: 18px;
    overflow: hidden;
    box-shadow: 0 6px 18px rgba(0,0,0,0.18);
  }
  .card--front { left: 40px; background: var(--white); }
  .card--back { left: 620px; background: var(--navy); }

  .front-wave { position: absolute; inset: 0; width: 100%; height: 100%; }

  .identity { position: absolute; left: 30px; top: 30px; }
  .identity__name {
    font-weight: 700; font-size: 19px; letter-spacing: 0.5px;
    color: var(--navy); text-transform: uppercase; line-height: 1.2;
  }
  .identity__role { font-size: 11px; color: var(--grey-text); margin-top: 2px; }

  .brand { position: absolute; display: flex; align-items: center; gap: 10px; }
  .brand--front { right: 34px; top: 56px; }
  .brand__mark { width: 30px; height: 30px; border-radius: 50%; background: var(--red); flex: none; }
  .brand__name {
    font-weight: 700; font-size: 18px; letter-spacing: 1px;
    color: var(--navy); text-transform: uppercase; line-height: 1.1;
  }

  .tagline {
    position: absolute; right: 34px; top: 112px;
    font-size: 9.5px; font-weight: 400; color: var(--grey-text);
    text-align: right; line-height: 1.4;
  }

  .contact { position: absolute; left: 30px; top: 238px; list-style: none; }
  .contact__item {
    display: flex; align-items: center; gap: 8px;
    font-size: 10.5px; color: var(--white); line-height: 1; margin-bottom: 6px;
  }
  .contact__icon {
    width: 13px; height: 13px; border-radius: 50%; background: var(--red);
    display: flex; align-items: center; justify-content: center; flex: none;
  }
  .contact__icon svg { width: 8px; height: 8px; }

  .service-area {
    position: absolute; right: 34px; top: 246px; text-align: right;
    font-size: 11px; color: var(--white); line-height: 1.45;
  }

  .brand--back {
    left: 50%; top: 92px; transform: translateX(-50%);
    flex-direction: column; gap: 12px;
  }
  .brand--back .brand__mark { width: 70px; height: 70px; background: var(--white); }
  .brand--back .brand__name { color: var(--white); font-size: 22px; text-align: center; white-space: nowrap; }

  .service-statement {
    position: absolute; left: 20px; right: 20px; bottom: 28px;
    text-align: center; font-size: 9px; color: var(--white); line-height: 1.6;
  }
</style>
</head>
<body>

<section class="card card--front" aria-label="Business card front">
  <svg class="front-wave" viewBox="0 0 540 310" preserveAspectRatio="none" aria-hidden="true">
    <path d="M0,186 C150,206 330,220 540,176" fill="none" stroke="var(--red)" stroke-width="6"/>
    <path d="M0,197 C150,217 330,231 540,187" fill="none" stroke="var(--navy)" stroke-width="3"/>
    <path d="M0,206 C150,226 330,240 540,196 L540,310 L0,310 Z" fill="var(--navy)"/>
  </svg>

  <div class="identity">
    <p class="identity__name">Dale Menschow</p>
    <p class="identity__role">Owner/CEO</p>
  </div>

  <div class="brand brand--front">
    <span class="brand__mark"></span>
    <span class="brand__name">Harborline<br>Energy</span>
  </div>

  <p class="tagline">Harborline Energy, Powering America's Oil &amp; Gas fields.</p>

  <ul class="contact">
    <li class="contact__item">
      <span class="contact__icon"><svg viewBox="0 0 10 10"><path d="M2 1 L4 1 L4.6 3 L3.5 4 Q4.5 6 6 6.5 L7 5.4 L9 6 L9 8 Q9 9 8 9 Q1 8.5 1 2 Q1 1 2 1Z" fill="#fff"/></svg></span>
      C: 555.318.4076
    </li>
    <li class="contact__item">
      <span class="contact__icon"><svg viewBox="0 0 10 10"><rect x="1" y="2.5" width="8" height="5.5" fill="#fff"/><path d="M1 2.5 L5 5.5 L9 2.5" fill="none" stroke="#c8202f" stroke-width="0.9"/></svg></span>
      E: Dmenschow@harborlineenergy.example
    </li>
    <li class="contact__item">
      <span class="contact__icon"><svg viewBox="0 0 10 10"><circle cx="5" cy="5" r="3.8" fill="none" stroke="#fff" stroke-width="1"/><path d="M1.2 5 H8.8 M5 1.2 Q2.8 5 5 8.8 M5 1.2 Q7.2 5 5 8.8" fill="none" stroke="#fff" stroke-width="0.8"/></svg></span>
      W: www.harborlineenergy.example
    </li>
  </ul>

  <p class="service-area">Servicing the Powder River<br>DJ basin and Bakken formations.</p>
</section>

<section class="card card--back" aria-label="Business card back">
  <div class="brand brand--back">
    <span class="brand__mark"></span>
    <span class="brand__name">Harborline Energy</span>
  </div>
  <p class="service-statement">
    • Frac fueling is what we do. • We understand how important diesel fuel is to your operation<br>
    • which is why our main service line is Frac fueling. • We assure our supply and stand by our service
  </p>
</section>

</body>
</html>
```